Visitenkarten und Briefpapier für Beratungsunternehmen
Zielgruppe
Führungskräfte im Gesundheits- und Sozialwesen-
Aufgabenstellung
Wir suchen ein Set aus Briefpapier und Visitenkarten zu umserem Logo. Beides darf (muss nicht) beidseitig gestaltet werden.

```html
<!DOCTYPE html>
<html lang="de">
<head>
<meta charset="utf-8">
<title>Briefpapier KELMARANT</title>
<link href="https://fonts.googleapis.com/css2?family=Open+Sans:wght@400;700&display=swap" rel="stylesheet">
<style>
:root{
  --green:#3f9a2c;
  --green-light:#8cc63f;
  --text:#333;
  --muted:#555;
  --rule:#e6efe0;
  --paper:#fff;
}
*{margin:0;padding:0;box-sizing:border-box}
html,body{width:847px;height:1200px;overflow:hidden;background:var(--paper)}
body{font-family:'Open Sans',Arial,sans-serif;color:var(--text);position:relative}
.header-band{position:absolute;left:693px;top:0;width:154px;height:150px;background:linear-gradient(180deg,var(--green) 0%,var(--green-light) 100%)}
.edge-line{position:absolute;left:828px;top:150px;width:2px;height:1050px;background:var(--rule)}
.brand{position:absolute;left:700px;top:374px;width:124px;display:flex;align-items:center;gap:6px;font-size:14px;font-weight:400;color:var(--muted);letter-spacing:0.3px}
.brand-mark{width:9px;height:9px;background:var(--muted);flex:none}
.sidebar{position:absolute;left:700px;top:416px;width:124px;font-size:9.5px;line-height:16px;color:var(--muted);white-space:nowrap}
.sidebar .gap{height:14px}
.sidebar .indent{padding-left:30px}
.row span:first-child{display:inline-block;width:30px}
.recipient{position:absolute;left:54px;top:184px;font-size:11.5px;line-height:16px;font-style:normal}
.salutation{position:absolute;left:54px;top:312px;width:600px;font-size:11.5px}
.date{position:absolute;right:0;top:0}
.body-text{position:absolute;left:54px;top:346px;width:600px;font-size:12px;line-height:16px}
.body-text p{margin-bottom:16px}
.signature{position:absolute;left:54px;top:904px;font-size:11.5px}
</style>
</head>
<body>
<div class="header-band"></div>
<div class="edge-line"></div>

<div class="brand">
  <span class="brand-mark"></span>
  <span class="brand-name">KELMARANT</span>
</div>

<aside class="sidebar">
  <div>KELMARANT UG (hg)</div>
  <div>Ostelweg 14</div>
  <div>56710 Lindbrück</div>
  <div>Geschäftsführerin</div>
  <div class="indent">Rena Volkmar</div>
  <div class="gap"></div>
  <div>Telefon 0170.48 62 19</div>
  <div class="row"><span>Fax</span><span>0170.48 62 20</span></div>
  <div class="indent">www.kelmarant.de</div>
  <div class="row"><span>eMail</span><span>info@kelmarant.de</span></div>
  <div class="gap"></div>
  <div>St.-Nr. 12/345/0000/8</div>
  <div>Finanzamt Lindbrück</div>
  <div>HRB-Nr. B 4471902</div>
  <div>Kreisbank Lindbrück</div>
  <div class="row"><span>Konto</span><span>123 456 78</span></div>
  <div class="row"><span>BLZ</span><span>999 00 00</span></div>
  <div>IBAN</div>
  <div>DE21 480 0000 0712</div>
  <div>SWIFT KRBLDE55</div>
</aside>

<address class="recipient">
  Month 00, 200x<br>Addressee Name<br>Company Name<br>1234 Anywhere Avenue<br>Suite #000<br>City, State 00000-0000<br>Country
</address>

<div class="salutation">Dear Addressee Name:<span class="date">Ort, der 01.02.03</span></div>

<main class="body-text">
  <p>Andipsum dipsum nostis nulpute magnissis niatie te molor adignis sequips uscipisit, sit vel ipsucing ent lut lan ulla feugait augueraesto odolore doluptatio cons dolor sismodo luptatuero do od dolore magnim dolor augiuro eu facilis ea core estrud eugiat velis ad tat dio odolor augue magna corting eugait enim venibh et, quatumsan hendre tincinisi tisisi dolute molorest atem velesequat alit aliquat, vel dolore facidnis dolore dignis dolorper il euglamconsed deliquamcon henis alis atum duis at.</p>
  <p>Bore del ute faccum verdil aorper sent alit, venis autet, quipsustio eugue vero dolore velendre euis nos nonse dolessim illa feum dolor sumsan ectet lortincin vulputat amet, qui esto conulput acil in eugait vel essequam zzriusto diam, velit wissit autat.</p>
  <p>Obore dolor incip ea conummy nulput vel ullan henisim am in ute erdiliqui ex ent et, quis auglat, commod tis enis num delit laor acing elis dolorer se eugue feu facinci liquis aut lut nulluptat er sum zzrit vulla consequis accum incidunt iusci blaortio odolorest pratum velluptate modit, quat. Ut nummodo exercilisl iriliqu ipsusto dolesequat. Ut wisl in ute consequam ad diam vulputpat lan hent vel doloreet utat ver si.</p>
  <p>Vullaorem iusci blamcon seniamcommy nit iureetum dolore con ea faccum iureet prat. In utat acidunt nullum venismolum ing exer iusci bla augue magna consequi tem veliquis nostion utpat.</p>
  <p>Do ea acilisis dolore min ercing endre consequat. Ero consequis ad euguerat, siscidunt laor sum iuscipis nulluoreet, velent lit amconul laorperit lore diatum dui bla facipit irit alis ad dolorpe rostrud tem essequat praesequam, coreet ip er sim dit, velisim inciliquam, quis adigna feugue dolore et irillaor.</p>
  <p>Adiam zzrit,</p>
</main>

<div class="signature">Ilvaro Temnasi</div>
</body>
</html>
```